Residential technology services web site

We are looking for a web design to represent our new company which provides RESIDENTIAL technology services, such as computer and tablet repair, maintenance, networking, training, etc (like FixCrew).
We are an upbeat, fun, professional organization that provides premium services to residential clients. Because the focus is on residential clients, the design should be modern (a little web2.0ish), easy to navigate, come off a little fun, but still inspire confidence that we are professionals who will get the job done right.
We are looking for four pages:
-home page
-services page highlighting some of the more common services
-about page
-template page that can be used to showcase each specific service in greater detail
Some sample sites:
laptop-mender-harbor.example - layout
sparkfixmaple - layout
helpowls.example - great site
pcvalor.example - layout
devicefix-athome.example
Home page should promote PC repair, Mac repair, tablet screen repair, tablet/computer training, pick up and delivery, mission statement, parental controls, wireless networking setup, computer hookups, anything else you think is enticing. Does not have to be all the above services, could use slider for select few. Non service items have to be included. Discreet twitter/fb social buttons. Discreet testimonial section (1-2 testimonials). If I think of more stuff I will add, or you can use your imagination. Ways to get service, phone, remote, onsite, in lab.
Should also mention xx% off for new customers
One of the slides should be our guarantee to customers.
Services page should highlight some common services and show ways of getting them (onsite, phone, remote). Other than highlighting select few it should also link to each of our other services. Add other stuff as you see necessary.
Template page for each service should display one service, list what a customer will receive with the service, and have three columns for price (remote, onsite, lab). Also have linkbacks to other services. FixCrews service page is a good example (but shouldn't be a replica): http://www.fixcrew.example/services/computers-networking/email-setup.aspx
About us page is just that, mission statement, place for us to type up our service pledge/guarantee, some other stuff if you can think of it.
You can use placeholder text for now. Feel free to use stock images if you must, I will buy them afterwards, you should really only need a couple at most.
Header should have logo obviously, which I will upload here. Call to action: "Bite Back!" and list phone number. A menu: Home Services About - make sure to make it so more buttons could be added later.
Footer should have the obvious, maybe mini menu, copyright, mission statement, link to privacy policy, etc.
After selecting a style/submission we like, we can go into more specifics for each page.
If I'm doing this project thing wrong, please let me know!
Target Market(s)
Inexperience computer users, tablet users, those unable to do own repairs
Industry/Entity Type
Residential
Requirements
Nice to have
- We want the website to be catchy and utilize our colors along with a generous amount of black. Don't want the site to be too light/white.

```html
<!DOCTYPE html>
<html lang="en">
<head>
<meta charset="UTF-8">
<title>NovaByte – Residential Technology Services</title>
<link href="https://fonts.googleapis.com/css2?family=Source+Sans+3:ital,wght@0,400;0,600;1,400;1,600;1,700&display=swap" rel="stylesheet">
<style>
:root{
  --green:#8cc63f;
  --green-dark:#5e9c1e;
  --green-light:#b5e061;
  --ink:#000;
  --panel:#1b1b1b;
  --band:#262626;
  --text:#d6d6d6;
  --muted:#8a8a8a;
  --white:#fff;
}
*{margin:0;padding:0;box-sizing:border-box}
html,body{width:1200px;height:1200px;overflow:hidden;background:var(--ink)}
body{font-family:"Source Sans 3",sans-serif;color:var(--white)}
.page{position:relative;width:1200px;height:1200px;overflow:hidden;background:var(--ink)}
.abs{position:absolute}

.hero-bg{left:0;top:0;width:1200px;height:470px;
  background:radial-gradient(ellipse 520px 330px at 780px 300px,#4a4a4a 0%,#2a2a2a 45%,#0c0c0c 100%)}
.header-band{left:0;top:0;width:1200px;height:100px;
  background:linear-gradient(#2e2e2e,#141414);border-radius:0 0 50% 50% / 0 0 14px 14px}
.logo-plate{left:118px;top:0;width:218px;height:167px}
.logo{left:140px;top:40px;display:flex;align-items:center;gap:8px;
  font-size:34px;font-weight:600;color:var(--green);letter-spacing:-.5px}
.logo-mark{width:16px;height:16px;background:var(--green)}

.call{left:705px;top:5px;font-size:20px;color:var(--white)}
.call span{color:var(--green)}
.search{left:928px;top:0;width:141px;height:23px;border-radius:0 0 8px 8px;
  background:linear-gradient(var(--green-light),var(--green));
  font-size:13px;font-style:italic;color:#fff;padding:3px 0 0 14px}
.search svg{position:absolute;right:8px;top:3px}

.nav{left:549px;top:60px;display:flex;gap:0;font-size:17px;font-style:italic;font-weight:600}
.nav a{color:var(--white);text-decoration:none;padding:5px 14px;height:29px;border-radius:6px}
.nav a.active{background:linear-gradient(var(--green-light),var(--green));padding:5px 17px}

.dropdown{left:716px;top:93px;width:259px;height:111px;background:#000;border-radius:0 0 8px 8px;
  padding:17px 13px;font-size:13.5px;font-style:italic;line-height:30px;color:#eee}

.hero-title{left:178px;top:183px;font-size:35px;font-style:italic;font-weight:600;color:#eee}
.hero-sub{left:177px;top:222px;font-size:23px;font-style:italic;font-weight:600;color:#eee}
.hero-text{left:179px;top:258px;width:340px;font-size:13px;font-style:italic;line-height:17px;color:#eee}
.btn{left:181px;top:330px;width:142px;height:40px;border-radius:7px;
  background:linear-gradient(var(--green-light),var(--green-dark));
  font-size:20px;font-style:italic;font-weight:600;color:#fff;text-align:center;line-height:38px}
.dots{left:186px;top:401px;display:flex;gap:10px}
.dots i{width:11px;height:11px;border-radius:50%;background:#fff}
.dots i:first-child{background:var(--green)}
.hero-visual{left:510px;top:238px;width:565px;height:215px;border-radius:8px 8px 3px 3px;
  background:linear-gradient(#3a3a3a,#c9cbd0 80%,#8d8f93)}

.panel{left:100px;top:440px;width:1000px;height:560px;background:var(--panel);border-radius:8px 8px 0 0}
.card{top:472px;width:316px}
.card .photo{height:163px;border-radius:8px}
.card h3{margin-top:8px;padding-left:5px;font-size:19.5px;font-style:italic;font-weight:600;color:var(--green)}
.card p{margin-top:4px;padding-left:5px;font-size:13px;line-height:18px;color:var(--text);text-align:justify}
.card .more{display:block;text-align:right;font-size:14px;font-style:italic;font-weight:600;color:var(--green);margin-top:1px}

.welcome-title{left:119px;top:777px;font-size:20.5px;font-style:italic;font-weight:600;color:var(--green)}
.welcome-text{left:120px;top:810px;width:636px;font-size:13px;line-height:24px;color:var(--text);text-align:justify}
.welcome-photo{left:771px;top:817px;width:291px;height:150px;border:3px solid #fff;border-radius:6px;
  background:linear-gradient(120deg,#e8ecef,#b9c3cc 60%,#4a5566)}

.partners{left:100px;top:996px;width:1000px;height:110px;background:linear-gradient(#2b2b2b,#1a1a1a)}
.partners h2{position:absolute;left:50px;top:30px;font-size:29px;font-weight:400;line-height:1}
.partners p{position:absolute;left:52px;top:62px;font-size:16px}
.badge{position:absolute;background:#555}
.arrow{position:absolute;left:895px;top:46px}

.footer-nav{left:138px;top:1150px;display:flex;gap:0;font-size:16px;font-style:italic}
.footer-nav a{text-decoration:none;color:var(--muted);margin-right:31px}
.footer-nav a.active{color:#fff;font-weight:600}
.follow{left:858px;top:1146px;font-size:15px;font-style:italic;color:#bbb;display:flex;align-items:center;gap:9px}
.social{width:20px;height:20px;border-radius:50%}
.copy{left:908px;top:1174px;font-size:12.5px;font-style:italic;font-weight:600;color:#fff}
</style>
</head>
<body>
<div class="page">
  <div class="abs hero-bg" role="img" aria-label="Dark grey radiating light background"></div>
  <div class="abs header-band"></div>
  <svg class="abs logo-plate" viewBox="0 0 218 167" aria-hidden="true">
    <polygon points="0,0 218,0 218,115 109,167 0,115" fill="#2d2d2d"/>
  </svg>
  <div class="abs logo"><span class="logo-mark"></span>NovaByte</div>

  <div class="abs call">CALL US : <span>025 555 0147</span></div>
  <div class="abs search">Search
    <svg width="18" height="18" viewBox="0 0 18 18"><circle cx="7" cy="7" r="5" fill="none" stroke="#fff" stroke-width="2.2"/><line x1="11" y1="11" x2="16" y2="16" stroke="#fff" stroke-width="2.6" stroke-linecap="round"/></svg>
  </div>

  <nav class="abs nav">
    <a class="active" href="#">Home</a><a href="#">About us</a><a href="#">Services</a><a href="#">Testimonials</a><a href="#">Blog</a><a href="#">Contact</a>
  </nav>
  <div class="abs dropdown">
    <div>Residential technology services</div>
    <div>Heaning fixing and repairing home PC</div>
    <div>networking</div>
  </div>

  <h1 class="abs hero-title">Sed ut perspiciatis unde</h1>
  <h2 class="abs hero-sub">Miste natus error sit</h2>
  <p class="abs hero-text">Sed ut perspiciatis unde omnis iste natus error sit volupta-tem accusantium doloremque laudantium, totam rem aperiam, eaque ipsa quae ab illo inventore veritatis</p>
  <div class="abs btn">Learn More</div>
  <div class="abs dots"><i></i><i></i><i></i></div>
  <div class="abs hero-visual" role="img" aria-label="Row of laptops, the front one showing a technician helping a client with a computer"></div>

  <div class="abs panel"></div>

  <article class="abs card" style="left:113px">
    <div class="photo" role="img" aria-label="Technician examining a computer monitor" style="background:linear-gradient(90deg,#9fb3c6,#e8f0f6 55%,#f4f8fb)"></div>
    <h3>Fixing and repairing home PC</h3>
    <p>Sed ut perspiciatis unde omnis iste natus error sit volupta-tem accusantium doloremque laudantium, totam rem aperiam</p>
    <a class="more">Read more...</a>
  </article>
  <article class="abs card" style="left:446px;width:313px">
    <div class="photo" role="img" aria-label="Two technicians working at a server rack" style="background:linear-gradient(90deg,#d9dde0,#3a3a35 50%,#c8ccd0)"></div>
    <h3>PC Networking</h3>
    <p>Sed ut perspiciatis unde omnis iste natus error sit volupta-tem accusantium doloremque laudantium, totam rem aperiam</p>
    <a class="more">Read more...</a>
  </article>
  <article class="abs card" style="left:772px">
    <div class="photo" role="img" aria-label="Network cables against glowing blue fibre optic lights" style="background:radial-gradient(circle at 70% 40%,#6fb6ea,#1d5c96 55%,#0b2340)"></div>
    <h3>How does it work</h3>
    <p>Sed ut perspiciatis unde omnis iste natus error sit volupta-tem accusantium doloremque laudantium, totam rem aperiam</p>
    <a class="more">Read more...</a>
  </article>

  <h2 class="abs welcome-title">WELCOME TO OUR WEBSITE</h2>
  <p class="abs welcome-text">Sed ut perspiciatis unde omnis iste natus error sit voluptatem accusantium doloremque laudantium, totam rem aperiam, eaque ipsa quae ab illo inventore veritatis et quasi architecto beatae vitae dicta sunt explicabo. Nemo enim ipsam consequunturSed ut perspiciatis unde omnis iste natus error sit voluptatem accusantium doloremque laudan-tium, totam rem aperiam, eaque ipsa quae ab illo inventore veritatis et quasi architecto beatae vitae dicta sunt expli-cabo. Nemo enim ipsam consequunturSed ut perspiciatis unde omnis iste natus error sit voluptatem accusantium doloremque laudantium, totam rem aperiam,</p>
  <div class="abs welcome-photo" role="img" aria-label="Two business people reviewing documents at a desk"></div>

  <section class="abs partners">
    <h2>Partners</h2>
    <p>We carry a wide selection of Partners</p>
    <div class="badge" style="left:320px;top:27px;width:106px;height:68px;border-radius:50%"></div>
    <div class="badge" style="left:455px;top:40px;width:146px;height:34px;border-radius:3px"></div>
    <div class="badge" style="left:633px;top:38px;width:92px;height:48px;border-radius:3px"></div>
    <div class="badge" style="left:753px;top:34px;width:120px;height:48px;border-radius:3px"></div>
    <svg class="arrow" width="14" height="24" viewBox="0 0 14 24" aria-hidden="true"><polyline points="3,2 12,12 3,22" fill="none" stroke="#444" stroke-width="3"/></svg>
  </section>

  <nav class="abs footer-nav">
    <a class="active" href="#">Home</a><a href="#">About us</a><a href="#">Services</a><a href="#">Testimonials</a><a href="#">Blog</a><a href="#">Contact</a>
  </nav>
  <div class="abs follow">Follow us :
    <span class="social" style="background:#3fa9e0"></span>
    <span class="social" style="background:#e0457b"></span>
    <span class="social" style="background:#3b5ba0"></span>
    <span class="social" style="background:#f08a1c"></span>
    <span class="social" style="background:#5fc3e8"></span>
  </div>
  <div class="abs copy">© 2012. www.novabyte.example</div>
</div>
</body>
</html>
```